Brightfernrx website

We are a weight loss clinic and we need a website built. please look at these websites for content and style. Just need like 5 pages see samples. AI files of logo are not avail yet so use sample for place set

https://glowshiftstudio.com/
ortanvital.com
https://pinecrestclinicalbodybalance.com/
https://yourslimmingnook.com/
https://qrvskinstudio.com/treatments/weight-loss-injections/

Target Market(s)

Women

Industry/Entity Type

weight loss

Coding

Coded - Design and coding required

Number of Pages Required

5+ page

Requirements
Nice to have
• please make look like a medspa website

```html
<!DOCTYPE html>
<html lang="en">
<head>
<meta charset="utf-8">
<title>Brightfernrx – Find Your Healthy Weight</title>
<link rel="stylesheet" href="https://fonts.googleapis.com/css2?family=Poppins:wght@300;400;500;600;700&display=swap">
<style>
:root{
  --green:#8bc34a;
  --green-dark:#6fa531;
  --blue:#1e8fd6;
  --ink:#1d1d1d;
  --muted:#777;
  --line:#e6e6e6;
  --soft:#f5f6f7;
  --black:#0b0b0b;
}
*{box-sizing:border-box;margin:0;padding:0}
html,body{width:1200px;height:3996px;overflow:hidden}
body{font-family:"Poppins",sans-serif;color:var(--ink);background:#fff;position:relative}
.eyebrow{color:var(--green);font-size:11px;font-weight:600;letter-spacing:1px;text-transform:uppercase}
.section-title{font-size:40px;font-weight:700;line-height:1.15}
.center{text-align:center}
.lead{color:var(--muted);font-size:13px;line-height:1.7}

/* header */
.site-header{position:absolute;top:0;left:0;width:1200px;height:84px;background:#fff;display:flex;align-items:center;padding:0 100px;z-index:2}
.brand{display:flex;align-items:center;gap:10px;font-size:26px;font-weight:700;color:var(--green-dark)}
.brand-dot{width:22px;height:22px;border-radius:50%;background:var(--green)}
.main-nav{display:flex;gap:34px;margin-left:130px;font-size:11px;font-weight:500;text-transform:uppercase}
.main-nav a{color:#444;text-decoration:none}
.main-nav a.active{color:var(--blue);border-bottom:2px solid var(--blue);padding-bottom:4px}
.header-contact{margin-left:auto;display:flex;align-items:center;gap:14px;font-size:12px}
.btn{display:inline-block;background:var(--blue);color:#fff;font-size:12px;font-weight:500;padding:12px 26px;border-radius:4px;text-decoration:none}
.icon-btn{width:38px;height:38px;background:var(--blue);border-radius:4px;display:flex;align-items:center;justify-content:center}

/* hero */
.hero{position:absolute;top:0;left:0;width:1200px;height:580px;background:linear-gradient(90deg,#2c2a29,#5a5350 45%,#3a3533);color:#fff;text-align:center}
.hero::after{content:"";position:absolute;inset:0;background:rgba(0,0,0,.35)}
.hero-photo{position:absolute;inset:0}
.hero-inner{position:relative;z-index:1;padding-top:170px}
.hero h1{font-size:66px;font-weight:700;line-height:1.15}
.hero h1 span{color:var(--green)}
.hero p{width:560px;margin:24px auto 32px;font-size:13px;line-height:1.7;color:#e8e8e8}

/* about */
.about{position:absolute;top:580px;left:0;width:1200px;height:700px}
.about-text{position:absolute;left:100px;top:80px;width:500px}
.about-text h2{margin:8px 0 22px;font-size:36px}
.about-text h2 span{color:var(--green)}
.feature-list{list-style:none;margin-top:26px}
.feature-list li{display:flex;gap:12px;margin-bottom:18px}
.feature-list b{display:block;font-size:14px;font-weight:600}
.feature-list small{color:var(--muted);font-size:11px;line-height:1.5;display:block}
.tick{flex:none;width:18px;height:18px;border-radius:50%;background:var(--green);margin-top:2px}
.about-photo{position:absolute;left:690px;top:50px;width:400px;height:560px;background:linear-gradient(180deg,#f3f1ef,#d9dbe2 70%,#b8c6d8);border-radius:4px}
.exp-badge{position:absolute;left:620px;top:200px;width:110px;height:120px;background:#eef3e4;text-align:center;padding-top:22px}
.exp-badge strong{display:block;font-size:34px;font-weight:700}
.exp-badge span{font-size:11px;color:var(--muted)}

/* offers */
.offers{position:absolute;top:1280px;left:0;width:1200px;height:620px;background:var(--soft);padding-top:60px}
.offers .lead{width:520px;margin:14px auto 0}
.offer-grid{display:grid;grid-template-columns:repeat(3,300px);gap:30px;justify-content:center;margin-top:44px}
.offer-card{background:#fff;height:160px;padding:28px 24px;box-shadow:0 4px 14px rgba(0,0,0,.05)}
.offer-head{display:flex;align-items:center;gap:14px;margin-bottom:14px}
.offer-head h3{font-size:14px;font-weight:600;line-height:1.3}
.offer-card p{font-size:11px;color:var(--muted);line-height:1.6}

/* goal */
.goal{position:absolute;top:1900px;left:0;width:1200px;height:480px}
.goal-photo{position:absolute;left:100px;top:60px;width:520px;height:360px;background:linear-gradient(120deg,#c9b7a3,#8f7f73 50%,#d9d3cb)}
.goal-text{position:absolute;left:650px;top:70px;width:430px;background:#fff;padding:20px 10px 0 0}
.goal-text h2{font-size:38px;margin:6px 0 16px}
.skill{margin-top:20px}
.skill-row{display:flex;justify-content:space-between;font-size:11px;font-weight:500;margin-bottom:7px}
.bar{height:5px;background:#e5e5e5}
.bar i{display:block;height:100%;background:var(--green)}

/* pricing */
.pricing{position:absolute;top:2380px;left:0;width:1200px;height:780px;padding-top:50px}
.pricing .lead{width:520px;margin:14px auto 0}
.plans{display:flex;justify-content:center;gap:30px;margin-top:44px}
.plan{width:316px;border:1px solid var(--line);text-align:center;background:#fff}
.plan-head{background:#f0f0f0;padding:26px 0 24px}
.plan-head h3{font-size:16px;font-weight:700}
.plan-head p{font-size:11px;color:var(--muted);margin:4px 0 16px}
.price{display:inline-flex;align-items:center;justify-content:center;width:96px;height:96px;border-radius:50%;background:#fff;font-size:32px;font-weight:700}
.price sup{font-size:12px;margin-left:2px}
.price small{font-size:9px;font-weight:400;color:var(--muted);margin-top:22px}
.plan.featured .plan-head{background:var(--green);color:#fff}
.plan.featured .plan-head p{color:#fff}
.plan.featured .price{color:var(--ink)}
.plan ul{list-style:none}
.plan li{font-size:12px;color:#555;padding:12px 0;border-bottom:1px solid var(--line)}
.plan .enroll{display:inline-block;margin:24px 0 30px;font-size:11px;padding:10px 22px;border-radius:3px;background:#eee;color:#333;text-decoration:none}
.plan.featured .enroll{background:var(--green);color:#fff}

/* reviews */
.reviews{position:absolute;top:3160px;left:0;width:1200px;height:380px;background:linear-gradient(180deg,#f3f3f3,#e9e9e9);padding-top:44px}
.review-grid{display:flex;justify-content:center;gap:36px;margin-top:36px}
.review{position:relative;width:480px;height:180px;background:#fff;padding:36px 60px;text-align:center}
.review p{font-size:15px;line-height:1.5;color:var(--ink)}
.review cite{display:block;margin-top:14px;font-style:normal;font-size:11px;color:var(--green-dark)}
.quote{position:absolute;font-size:90px;font-weight:700;color:#d5d5d5;line-height:1}
.quote.open{left:12px;top:10px}
.quote.close{right:12px;bottom:-30px}

/* footer */
.site-footer{position:absolute;top:3540px;left:0;width:1200px;height:456px;background:var(--black);color:#fff;text-align:center;padding-top:80px}
.site-footer .brand{justify-content:center;color:#fff}
.footer-about{width:480px;margin:24px auto 50px;font-size:12px;line-height:1.7;color:#cfcfcf}
.footer-contact{display:flex;justify-content:center;gap:40px;font-size:15px}
.footer-bottom{position:absolute;left:100px;right:100px;bottom:0;height:70px;border-top:1px solid #2a2a2a;display:flex;align-items:center;justify-content:space-between;font-size:11px;color:#aaa}
.socials{display:flex;gap:8px}
.socials span{width:22px;height:22px;border-radius:50%;background:#fff}
</style>
</head>
<body>

<section class="hero">
  <div class="hero-photo" role="img" aria-label="Photo of a woman measuring her waist with a tape"></div>
  <div class="hero-inner">
    <h1>Find Your <span>Healthy</span><br>Weight.</h1>
    <p>It is a long established fact that a balanced plan and steady support help you reach a healthier weight, at your pace and in your own way.</p>
    <a class="btn" href="#">Start Your Weight Loss Journey</a>
  </div>
</section>

<header class="site-header">
  <div class="brand"><span class="brand-dot"></span>Brightfernrx</div>
  <nav class="main-nav">
    <a class="active" href="#">Home</a><a href="#">Services</a><a href="#">Treatments</a><a href="#">About Us</a><a href="#">Contact Us</a>
  </nav>
  <div class="header-contact">
    <svg width="16" height="16" viewBox="0 0 24 24" fill="none" stroke="#1e8fd6" stroke-width="2"><path d="M5 3h4l2 5-3 2a11 11 0 0 0 6 6l2-3 5 2v4a2 2 0 0 1-2 2A17 17 0 0 1 3 5a2 2 0 0 1 2-2z"/></svg>
    <span>555.014.2290</span>
    <div class="icon-btn"><svg width="16" height="16" viewBox="0 0 24 24" fill="none" stroke="#fff" stroke-width="2"><circle cx="11" cy="11" r="7"/><path d="M16 16l5 5"/></svg></div>
  </div>
</header>

<section class="about">
  <div class="about-text">
    <div class="eyebrow">About Us</div>
    <h2 class="section-title">Welcome to <span>Brightfernrx</span><br>Your weight loss support</h2>
    <p class="lead">Our clinic offers medically guided weight loss in a calm, spa-like setting. Each plan is shaped around your body, your goals and your daily routine, with care from people who listen and follow up at every step of the way.</p>
    <ul class="feature-list">
      <li><span class="tick"></span><div><b>Best Weight Loss Service</b><small>Guided care from our clinical team, with regular check-ins.</small></div></li>
      <li><span class="tick"></span><div><b>Find Your Weight Loss Services</b><small>Injections, nutrition and coaching matched to your needs.</small></div></li>
      <li><span class="tick"></span><div><b>Individual Weight Loss Programs</b><small>A personal plan built around your schedule and goals.</small></div></li>
    </ul>
  </div>
  <div class="about-photo" role="img" aria-label="Photo of a smiling woman in workout clothes sitting on an exercise ball holding a water bottle"></div>
  <div class="exp-badge"><strong>15</strong><span>Years<br>Experience</span></div>
</section>

<section class="offers">
  <div class="eyebrow center">Our Service</div>
  <h2 class="section-title center">What We Offer</h2>
  <p class="lead center">Care that fits your life, from first visit to lasting results. Explore the services our team provides.</p>
  <div class="offer-grid">
    <div class="offer-card"><div class="offer-head"><svg width="40" height="40" viewBox="0 0 40 40" fill="none" stroke="#1e8fd6" stroke-width="2"><rect x="6" y="8" width="28" height="26" rx="4"/><circle cx="20" cy="20" r="6"/></svg><h3>Weight Loss<br>Program</h3></div><p>Structured steps with medical guidance and weekly progress checks to keep you moving.</p></div>
    <div class="offer-card"><div class="offer-head"><svg width="40" height="40" viewBox="0 0 40 40" fill="none" stroke="#1e8fd6" stroke-width="2"><circle cx="20" cy="22" r="12"/><path d="M20 10v-5"/></svg><h3>Personalized<br>Nutrition</h3></div><p>Meal plans built around foods you enjoy, balanced to support steady, lasting change.</p></div>
    <div class="offer-card"><div class="offer-head"><svg width="40" height="40" viewBox="0 0 40 40" fill="none" stroke="#1e8fd6" stroke-width="2"><path d="M6 20h28M10 13v14M30 13v14"/></svg><h3>Individual Workout<br>Coaching</h3></div><p>One to one sessions that match your fitness level and grow with your strength.</p></div>
    <div class="offer-card"><div class="offer-head"><svg width="40" height="40" viewBox="0 0 40 40" fill="none" stroke="#1e8fd6" stroke-width="2"><circle cx="20" cy="20" r="13"/><path d="M14 20l4 4 8-8"/></svg><h3>Sports<br>Nutritionist</h3></div><p>Fuel for training and recovery, planned by a specialist who knows active bodies.</p></div>
    <div class="offer-card"><div class="offer-head"><svg width="40" height="40" viewBox="0 0 40 40" fill="none" stroke="#1e8fd6" stroke-width="2"><circle cx="20" cy="14" r="6"/><path d="M9 34c2-8 20-8 22 0"/></svg><h3>Child<br>Nutrition</h3></div><p>Gentle guidance on healthy eating habits for children and the whole family.</p></div>
    <div class="offer-card"><div class="offer-head"><svg width="40" height="40" viewBox="0 0 40 40" fill="none" stroke="#1e8fd6" stroke-width="2"><path d="M6 18l14-11 14 11v16H6z"/></svg><h3>In-Home Massage<br>Therapy</h3></div><p>Relaxing treatments brought to your home to ease tension and aid recovery.</p></div>
  </div>
</section>

<section class="goal">
  <div class="goal-photo" role="img" aria-label="Photo of women in a group fitness class with exercise balls"></div>
  <div class="goal-text">
    <div class="eyebrow">Our Expertise</div>
    <h2 class="section-title">A goal without a plan<br>is just a wish</h2>
    <p class="lead">We turn your goals into clear daily steps, with support that keeps you on track.</p>
    <div class="skill"><div class="skill-row"><span>Healthy Exercise</span><span>70%</span></div><div class="bar"><i style="width:70%"></i></div></div>
    <div class="skill"><div class="skill-row"><span>Nutrition &amp; Lifestyle</span><span>90%</span></div><div class="bar"><i style="width:90%"></i></div></div>
    <div class="skill"><div class="skill-row"><span>Weight Management</span><span>80%</span></div><div class="bar"><i style="width:80%"></i></div></div>
  </div>
</section>

<section class="pricing">
  <div class="eyebrow center">Our Pricing</div>
  <h2 class="section-title center">Choose Pack</h2>
  <p class="lead center">Simple monthly plans with everything you need to begin. Pick the level of support that suits you.</p>
  <div class="plans">
    <div class="plan"><div class="plan-head"><h3>PRIMARY MEMBERSHIP</h3><p>Self Directed Training</p><span class="price">$99<sup>.99</sup><small>/Month</small></span></div>
      <ul><li>Self Directed Training</li><li>Weight Training Sets</li><li>General Assistance</li><li>Diet Guides</li><li>Basic Stretching</li></ul><a class="enroll" href="#">Enroll Now</a></div>
    <div class="plan featured"><div class="plan-head"><h3>PRIMARY MEMBERSHIP</h3><p>Self Directed Training</p><span class="price">$99<sup>.99</sup><small>/Month</small></span></div>
      <ul><li>Self Directed Training</li><li>Weight Training Sets</li><li>General Assistance</li><li>Diet Guides</li><li>Basic Stretching</li></ul><a class="enroll" href="#">Enroll Now</a></div>
    <div class="plan"><div class="plan-head"><h3>PRIMARY MEMBERSHIP</h3><p>Self Directed Training</p><span class="price">$99<sup>.99</sup><small>/Month</small></span></div>
      <ul><li>Self Directed Training</li><li>Weight Training Sets</li><li>General Assistance</li><li>Diet Guides</li><li>Basic Stretching</li></ul><a class="enroll" href="#">Enroll Now</a></div>
  </div>
</section>

<section class="reviews">
  <div class="eyebrow center">Client Says</div>
  <h2 class="section-title center">Choose Latest Reviews</h2>
  <div class="review-grid">
    <blockquote class="review"><span class="quote open">“</span><p>Those who think they have no time for bodily exercise will sooner or later have to find time for illness.</p><cite>~ Maren Ellis ~</cite><span class="quote close">”</span></blockquote>
    <blockquote class="review"><span class="quote open">“</span><p>Those who think they have no time for bodily exercise will sooner or later have to find time for illness.</p><cite>~ Maren Ellis ~</cite><span class="quote close">”</span></blockquote>
  </div>
</section>

<footer class="site-footer">
  <div class="brand"><span class="brand-dot"></span>Brightfernrx</div>
  <p class="footer-about">A caring weight loss clinic helping women feel strong, healthy and confident in a calm setting.</p>
  <div class="footer-contact">
    <span>555.014.2290</span><span>|</span><span>info@brightfernrx.com</span>
  </div>
  <div class="footer-bottom">
    <span>@Copyright Brightfernrx 2022. All rights reserved</span>
    <div class="socials"><span></span><span></span><span></span><span></span></div>
  </div>
</footer>

</body>
</html>
```